New business card for civil engineering company - "Keel Survey"

We need a business card designed for our new structural engineering company.

The company name is "Keel Survey" logo files attached.

We would like the following:
* Two-sided card
* Simple design

Information to be placed on the card:
Name - Marcus Hollby
Job Title - Director / Structural Engineer
Credentials - BEng(Hons), CPEng, CMengNZ, IntPE(NZ)
Email - marcus.hollby@keelsurvey-example.co.nz
mobile - 0219036458
website - www.keelsurvey-example.co.nz

```html
<!DOCTYPE html>
<html lang="en">
<head>
<meta charset="utf-8">
<title>Keel Survey — Business Card</title>
<link href="https://fonts.googleapis.com/css2?family=Montserrat:wght@400;500&display=swap" rel="stylesheet">
<style>
  :root {
    --stage: #77787c;
    --card-dark: #38383b;
    --card-blue-top: #0c4778;
    --card-blue-bottom: #063a6b;
    --accent: #3a9bd5;
    --white: #ffffff;
    --muted: #8b8b90;
    --faint-brand: #3b6594;
  }
  * { margin: 0; padding: 0; box-sizing: border-box; }
  html, body {
    width: 1200px; height: 1200px; overflow: hidden;
    background: var(--stage);
    font-family: "Montserrat", sans-serif;
  }
  .card {
    position: absolute; top: 202px;
    width: 456px; height: 798px;
  }
  .card--front { left: 94px; background: var(--card-dark); }
  .card--back {
    left: 646px;
    background: linear-gradient(160deg, var(--card-blue-top), var(--card-blue-bottom));
  }
  .front-block { position: absolute; right: 56px; text-align: right; }
  .brand-name {
    font-weight: 500; font-size: 31px; letter-spacing: 4px;
    color: var(--white); text-transform: uppercase; line-height: 1;
  }
  .brand-tagline {
    font-size: 13px; letter-spacing: 3.4px; color: var(--muted);
    text-transform: uppercase; line-height: 1;
  }
  .front-brand { top: 290px; }
  .front-brand .brand-tagline { margin-top: 10px; }
  .divider {
    position: absolute; top: 410px; right: 56px;
    width: 23px; height: 3px; background: var(--accent);
  }
  .person { top: 462px; line-height: 1.3; }
  .person-name {
    font-size: 25px; letter-spacing: 2.4px; color: var(--accent);
    text-transform: uppercase; line-height: 1.1; margin-bottom: 2px;
  }
  .person-title { font-size: 19.5px; color: var(--white); }
  .person-credentials { font-size: 19.5px; color: var(--accent); }
  .contacts { top: 618px; list-style: none; }
  .contact {
    display: flex; justify-content: flex-end; align-items: center;
    gap: 14px; font-size: 18px; color: var(--white); height: 30px;
  }
  .contact .highlight { color: var(--accent); }
  .contact svg { width: 20px; height: 20px; flex: none; }
  .back-brand { position: absolute; left: 34px; top: 652px; }
  .back-brand .brand-name { color: var(--faint-brand); font-size: 32px; }
  .back-brand .brand-tagline { color: var(--faint-brand); margin-top: 12px; font-size: 14px; }
</style>
</head>
<body>
  <section class="card card--front" aria-label="Card front">
    <div class="front-block front-brand">
      <div class="brand-name">Keel Survey</div>
      <div class="brand-tagline">Peer Review Specialists</div>
    </div>
    <div class="divider"></div>
    <div class="front-block person">
      <div class="person-name">Marcus Hollby</div>
      <div class="person-title">Director / Structural Engineer</div>
      <div class="person-credentials">BEng(Hons), CPEng, CMengNZ<br>IntPE(NZ)</div>
    </div>
    <ul class="front-block contacts">
      <li class="contact">0219 036 458
        <svg viewBox="0 0 20 20" fill="none" stroke="#3a9bd5" stroke-width="1.8"><rect x="5" y="1" width="10" height="18" rx="1.5"/><circle cx="10" cy="15.5" r="0.8" fill="#3a9bd5"/></svg>
      </li>
      <li class="contact">marcus.hollby@keelsurvey-example.co.nz
        <svg viewBox="0 0 20 20" fill="none" stroke="#3a9bd5" stroke-width="1.6"><rect x="1.5" y="4.5" width="17" height="11"/><path d="M1.5 4.5 L10 11 L18.5 4.5"/></svg>
      </li>
      <li class="contact"><span>www.<span class="highlight">keelsurvey-example</span>.co.nz</span>
        <svg viewBox="0 0 20 20" fill="none" stroke="#3a9bd5" stroke-width="1.4"><circle cx="10" cy="10" r="8.5"/><ellipse cx="10" cy="10" rx="4" ry="8.5"/><path d="M1.5 10 H18.5 M3 5.5 H17 M3 14.5 H17"/></svg>
      </li>
    </ul>
  </section>

  <section class="card card--back" aria-label="Card back">
    <div class="back-brand">
      <div class="brand-name">Keel Survey</div>
      <div class="brand-tagline">Peer Review Specialists</div>
    </div>
  </section>
</body>
</html>
```